Disability provider requiring digital flyer to promote services

My company works within the Disability sector (QCWP registered provider), currently operating in Sydney, Australia.
I require a digital brochure which lists our services and gives potential customers a quick look into what we do with a single glance.
Undecided whether this digital flyer is to be single or double sided, happy to consult with an experienced designer in this regard.
I prefer minimalist designs (which may be an issue for someone trying to convey information, I'm not sure), and possibly someone who can work with out watercolor logo.
Services include:
-Supported Independent Living
-Specialist Disability Accommodation
-Individualised Living Options Stage 1 & 2
-Home Modifications
-Occupational Therapy
-Support Coordination Levels 1 & 2
-Short Term Accommodation - STA Respite
-Drop In Supports
-Community Access

```html
<!DOCTYPE html>
<html lang="en">
<head>
<meta charset="utf-8">
<title>Sunvale Care – Services Flyer</title>
<link rel="stylesheet" href="https://fonts.googleapis.com/css2?family=Oswald:wght@300;400;600&family=Josefin+Sans:wght@300;400&display=swap">
<style>
  :root {
    --backdrop: #e9e6e6;
    --paper: #f1f1f1;
    --ink: #55595d;
    --ink-soft: #6b6e71;
    --teal: #1fb5d6;
    --teal-frame: #5fc4c6;
    --sun: #f4c97a;
    --magenta: #dc3a96;
    --slate: #6c6e70;
    --rule: #707274;
    --mist: #dcdcdc;
  }
  * { box-sizing: border-box; margin: 0; padding: 0; }
  html, body { width: 1200px; height: 1036px; overflow: hidden; }
  body {
    background: var(--backdrop);
    font-family: "Oswald", sans-serif;
    position: relative;
  }
  .flyer {
    position: absolute;
    left: 240px; top: 18px;
    width: 720px; height: 1000px;
    background: var(--paper);
    overflow: hidden;
    box-shadow: 0 6px 24px rgba(0,0,0,.15);
  }
  .hero-art {
    position: absolute; left: 0; top: 30px; width: 720px; height: 260px;
    background: linear-gradient(100deg, #eaa3cf 0%, #f3c7a0 45%, #f6dcc0 70%, #bfe4ee 100%);
    opacity: .55;
  }
  .brand {
    position: absolute; right: 40px; top: 92px;
    display: flex; flex-direction: column; align-items: flex-end;
    z-index: 2;
  }
  .brand-name {
    font-family: "Josefin Sans", sans-serif; font-weight: 300;
    font-size: 64px; letter-spacing: -1px; color: var(--ink); line-height: 1;
  }
  .brand-sub {
    font-family: "Josefin Sans", sans-serif; font-weight: 300;
    font-size: 22px; letter-spacing: 14px; color: var(--ink); margin-top: 4px;
  }
  .tab { position: absolute; border-radius: 14px 50px 14px 50px; }
  .tab-sun { left: 250px; top: 318px; width: 200px; height: 100px; background: var(--sun); }
  .tab-magenta { left: 592px; top: 400px; width: 128px; height: 90px; background: var(--magenta); }
  .tab-slate { left: 205px; top: 600px; width: 180px; height: 100px; background: var(--slate); }
  .photo {
    position: absolute;
    border: 5px solid var(--teal-frame);
    border-top-color: var(--teal);
    border-radius: 14px 80px 14px 80px;
  }
  .photo-park { left: 20px; top: 405px; width: 325px; height: 200px;
    background: linear-gradient(135deg, #7a8a4c, #3f64a8 55%, #d9d2c8); }
  .photo-home { left: 350px; top: 368px; width: 240px; height: 190px;
    background: linear-gradient(135deg, #e5e3e0, #a9b4c0 55%, #8a3a34); }
  .photo-friends { left: 425px; top: 556px; width: 280px; height: 200px;
    background: linear-gradient(135deg, #8c3a30, #c99a8a 50%, #b8b8bc); }
  .backdrop-art {
    position: absolute; left: 180px; top: 620px; width: 540px; height: 300px;
    background: linear-gradient(180deg, rgba(200,200,200,0), rgba(200,200,200,.35));
  }
  .grass {
    position: absolute; left: 0; bottom: 0; width: 720px; height: 40px;
    background: linear-gradient(180deg, rgba(220,220,220,0), var(--mist));
  }
  .rule {
    position: absolute; left: 0; top: 792px; width: 720px; height: 4px; background: var(--rule);
  }
  .services-title {
    position: absolute; left: 56px; top: 770px;
    background: var(--slate); color: var(--sun);
    font-weight: 600; font-size: 30px; line-height: 1;
    padding: 9px 22px;
    border-radius: 24px 8px 24px 8px;
    text-transform: uppercase; letter-spacing: .3px;
    z-index: 2;
  }
  .service-list {
    position: absolute; top: 834px; list-style: none; z-index: 2;
    font-weight: 300; font-size: 19px; color: var(--ink-soft); line-height: 27px;
  }
  .service-list.col-a { left: 62px; }
  .service-list.col-b { left: 392px; }
  .service-list li { display: flex; align-items: center; gap: 10px; }
  .service-list svg { width: 16px; height: 16px; flex: none; }
</style>
</head>
<body>
  <main class="flyer">
    <div class="hero-art" role="img" aria-label="Watercolour illustration: tree with a swing, birds, butterflies and a carer with a person in a wheelchair on a grassy bank"></div>

    <div class="brand">
      <span class="brand-name">SUNVALE</span>
      <span class="brand-sub">CARE</span>
    </div>

    <div class="backdrop-art" role="img" aria-label="Faint grey illustration of a tree, swing and wheelchair user"></div>

    <div class="tab tab-sun"></div>
    <div class="tab tab-magenta"></div>
    <div class="tab tab-slate"></div>

    <div class="photo photo-park" role="img" aria-label="Photo of a carer chatting with an older man in a wheelchair in a park"></div>
    <div class="photo photo-home" role="img" aria-label="Photo of a woman dancing with a man in a wheelchair at home"></div>
    <div class="photo photo-friends" role="img" aria-label="Photo of two young women together by a window"></div>

    <div class="grass" role="img" aria-label="Soft grey grass edge along the bottom"></div>

    <div class="rule"></div>
    <h2 class="services-title">Services we provided</h2>

    <ul class="service-list col-a">
      <li><svg viewBox="0 0 16 16"><circle cx="8" cy="8" r="6" fill="none" stroke="#1fb5d6" stroke-width="3"/></svg>Supported Independent Living</li>
      <li><svg viewBox="0 0 16 16"><circle cx="8" cy="8" r="6" fill="none" stroke="#1fb5d6" stroke-width="3"/></svg>Specialist Disability Accommodation</li>
      <li><svg viewBox="0 0 16 16"><circle cx="8" cy="8" r="6" fill="none" stroke="#1fb5d6" stroke-width="3"/></svg>Individualised Living Options Stage 1 &amp; 2</li>
      <li><svg viewBox="0 0 16 16"><circle cx="8" cy="8" r="6" fill="none" stroke="#1fb5d6" stroke-width="3"/></svg>Home Modifications</li>
    </ul>
    <ul class="service-list col-b">
      <li><svg viewBox="0 0 16 16"><circle cx="8" cy="8" r="6" fill="none" stroke="#1fb5d6" stroke-width="3"/></svg>Occupational Therapy</li>
      <li><svg viewBox="0 0 16 16"><circle cx="8" cy="8" r="6" fill="none" stroke="#1fb5d6" stroke-width="3"/></svg>Support Coordination Levels 1 &amp; 2</li>
      <li><svg viewBox="0 0 16 16"><circle cx="8" cy="8" r="6" fill="none" stroke="#1fb5d6" stroke-width="3"/></svg>Short Term Accommodation - STA Respite</li>
      <li><svg viewBox="0 0 16 16"><circle cx="8" cy="8" r="6" fill="none" stroke="#1fb5d6" stroke-width="3"/></svg>Drop In Supports</li>
      <li><svg viewBox="0 0 16 16"><circle cx="8" cy="8" r="6" fill="none" stroke="#1fb5d6" stroke-width="3"/></svg>Community Access</li>
    </ul>
  </main>
</body>
</html>
```